Card Design for my dog training business Rustpaw Obedience

Need a business card design for my dog training business with my new logo. Want the card to come off professional yet fun. Want it to be very eye catchy as well. I normally have these at vet clinics, pet stores, and groomers. so need it to look better than my competitors.
Target Market(s)
dog owners
Industry/Entity Type
Dog Training
Contact Information for Business Card
needs logo, my name and info
Font styles to use
Serif
Colors
0255a3
ffffff
ec1f27
000000
333333
fbfbfb
Requirements
Must have
- Rustpaw Obedience
- Hollis Brandt
- 415 903 2267
- info@rustpawobedience.example
- www.rustpawobedience.example

```html
<!DOCTYPE html>
<html lang="en">
<head>
<meta charset="utf-8">
<title>Rustpaw Obedience — Business Card</title>
<link rel="stylesheet" href="https://fonts.googleapis.com/css2?family=Cinzel:wght@400;600&family=Crimson+Pro:ital,wght@0,400;0,500;1,400&display=swap">
<style>
  :root {
    --brand-blue: #0255a3;
    --card-blue: #3a55b0;
    --brand-red: #ec1f27;
    --white: #ffffff;
    --paper: #fbfbfb;
    --ink: #000000;
    --ink-soft: #333333;
    --pattern-grey: #ededed;
    --stage: #1c1c1c;
  }
  * { box-sizing: border-box; margin: 0; padding: 0; }
  html, body { width: 1200px; height: 1200px; overflow: hidden; background: var(--stage); }
  .stage {
    width: 1200px; height: 1200px;
    display: flex; flex-direction: column; align-items: center; justify-content: center; gap: 44px;
  }
  .card { position: relative; width: 900px; height: 514px; overflow: hidden; box-shadow: 0 10px 28px rgba(0,0,0,.55); }

  /* Back side */
  .card-back { background: var(--card-blue); }
  .card-back .pattern-fill {
    position: absolute; inset: 0;
    background: radial-gradient(ellipse at center, #4560bb 0%, var(--card-blue) 70%);
  }
  .card-back .brand-lockup {
    position: absolute; left: 0; right: 0; top: 150px;
    display: flex; flex-direction: column; align-items: center;
  }
  .brand-name {
    font-family: "Cinzel", serif; font-weight: 400; letter-spacing: 4px; line-height: 1.05; text-align: center;
  }
  .card-back .brand-name { color: var(--white); font-size: 56px; }
  .card-back .tagline {
    position: absolute; left: 0; right: 0; top: 350px; text-align: center;
    font-family: "Crimson Pro", serif; font-style: italic; font-size: 22px; color: var(--white); letter-spacing: .5px;
  }

  /* Front side */
  .card-front { background: var(--paper); }
  .card-front .pattern-fill {
    position: absolute; inset: 0;
    background: linear-gradient(135deg, var(--paper) 0%, var(--pattern-grey) 50%, var(--paper) 100%);
  }
  .name-tab { position: absolute; top: 48px; left: 0; display: flex; align-items: center; gap: 14px; }
  .name-tab .accent-square { width: 52px; height: 48px; background: var(--brand-red); }
  .name-tab .name-box {
    background: var(--card-blue); color: var(--white);
    font-family: "Cinzel", serif; font-weight: 600; font-size: 34px; letter-spacing: 1.5px;
    padding: 8px 22px 6px;
  }
  .contact-list { position: absolute; top: 152px; left: 46px; list-style: none; display: flex; flex-direction: column; gap: 14px; }
  .contact-item {
    display: flex; align-items: center; gap: 18px;
    font-family: "Crimson Pro", serif; font-size: 26px; line-height: 1; color: var(--ink-soft);
  }
  .contact-icon { width: 38px; height: 38px; border-radius: 50%; background: var(--brand-red); display: flex; align-items: center; justify-content: center; flex: none; }
  .contact-icon svg { width: 20px; height: 20px; }
  .card-front .brand-lockup {
    position: absolute; right: 46px; top: 170px; width: 330px;
    display: flex; flex-direction: column; align-items: center;
  }
  .card-front .brand-name { color: var(--ink); font-size: 44px; letter-spacing: 3px; }
  .footer-band { position: absolute; left: 0; bottom: 0; width: 900px; height: 200px; }
  .service-line {
    position: absolute; right: 50px; bottom: 34px; display: flex; align-items: center; gap: 12px;
    font-family: "Cinzel", serif; font-size: 24px; color: var(--white); letter-spacing: 1px;
  }
  .service-line svg { width: 22px; height: 22px; }
</style>
</head>
<body>
<main class="stage">

  <section class="card card-back" aria-label="Card back">
    <div class="pattern-fill" role="img" aria-label="Faint pattern of pet icons: dogs, bones, paws, dog houses, collars and grooming tools"></div>
    <div class="brand-lockup">
      <div class="brand-name">RUSTPAW<br>OBEDIENCE</div>
    </div>
    <p class="tagline">“Training dogs across Texas one dog at a time.”</p>
  </section>

  <section class="card card-front" aria-label="Card front">
    <div class="pattern-fill" role="img" aria-label="Faint grey pattern of pet icons: dogs, bones, paws, dog houses, collars and grooming tools"></div>

    <div class="name-tab">
      <span class="accent-square"></span>
      <h1 class="name-box">HOLLIS BRANDT</h1>
    </div>

    <ul class="contact-list">
      <li class="contact-item">
        <span class="contact-icon"><svg viewBox="0 0 24 24"><path fill="#fff" d="M6.6 10.8a15 15 0 0 0 6.6 6.6l2.2-2.2c.3-.3.7-.4 1-.2 1.1.4 2.3.6 3.6.6.6 0 1 .4 1 1V20c0 .6-.4 1-1 1A17 17 0 0 1 3 4c0-.6.4-1 1-1h3.5c.6 0 1 .4 1 1 0 1.3.2 2.5.6 3.6.1.3 0 .7-.2 1z"/></svg></span>
        415 903 2267
      </li>
      <li class="contact-item">
        <span class="contact-icon"><svg viewBox="0 0 24 24"><rect x="3" y="6" width="18" height="12" fill="none" stroke="#fff" stroke-width="2"/><path d="M3 6l9 7 9-7" fill="none" stroke="#fff" stroke-width="2"/></svg></span>
        info@rustpawobedience.example
      </li>
      <li class="contact-item">
        <span class="contact-icon"><svg viewBox="0 0 24 24" fill="none" stroke="#fff" stroke-width="1.8"><circle cx="12" cy="12" r="9"/><ellipse cx="12" cy="12" rx="4" ry="9"/><path d="M3 12h18M5 7.5h14M5 16.5h14"/></svg></span>
        www.rustpawobedience.example
      </li>
    </ul>

    <div class="brand-lockup">
      <div class="brand-name">RUSTPAW<br>OBEDIENCE</div>
    </div>

    <svg class="footer-band" viewBox="0 0 900 200" preserveAspectRatio="none" aria-hidden="true">
      <path d="M0 20 Q 320 30 640 110 L 640 112 Q 320 60 0 58 Z" fill="var(--card-blue)"/>
      <path d="M0 62 Q 360 70 620 118 Q 800 150 900 120 L 900 200 L 0 200 Z" fill="var(--brand-red)"/>
    </svg>

    <div class="service-line">
      <svg viewBox="0 0 24 24" fill="#fff"><ellipse cx="12" cy="16" rx="5" ry="4"/><circle cx="5" cy="10" r="2.2"/><circle cx="9.5" cy="6" r="2.2"/><circle cx="14.5" cy="6" r="2.2"/><circle cx="19" cy="10" r="2.2"/></svg>
      <span>VET CLINICS</span>
      <svg viewBox="0 0 24 24" fill="#fff"><ellipse cx="12" cy="16" rx="5" ry="4"/><circle cx="5" cy="10" r="2.2"/><circle cx="9.5" cy="6" r="2.2"/><circle cx="14.5" cy="6" r="2.2"/><circle cx="19" cy="10" r="2.2"/></svg>
      <span>PET STORES</span>
      <svg viewBox="0 0 24 24" fill="#fff"><ellipse cx="12" cy="16" rx="5" ry="4"/><circle cx="5" cy="10" r="2.2"/><circle cx="9.5" cy="6" r="2.2"/><circle cx="14.5" cy="6" r="2.2"/><circle cx="19" cy="10" r="2.2"/></svg>
      <span>GROOMERS.</span>
    </div>
  </section>

</main>
</body>
</html>
```